world's hottest chilli salt 7 flavours

I am needing a packaging design for 7 different ones to reflect our range

We are located in Perth OZ. Our chilli salts are new and unique and the world’s hottest ones as we use the world’s hottest chillies. Our product is made from chilli and salts but then other flavours to make them different - one for example is a Smokey one which is very popular and it made from salt, chilli, chipotle, coriander, yellow mustard seeds and garlic.

the colour distinguishes the difference between the different flavours

ingredient list is on the website for each flavour
please view fernmoltaskel.com at our range of chilli salts

Target Market(s)

Male adults age is from 18 + - target market is Australian market but will be selling overseas as well to the US.

Industry/Entity Type

Product

Requirements
Must have
• must be colour code as examples i have uploaded whether or to view fernmoltaskels.com -it it bigger or small i'm not fussed but there needs to be a distinction between the 7 different flavours. Size of label is 95mm x 37mm to work from so very small. The relish the blaze (attached) needs to be somewhere on the logo but i would like to see what someone can do with that.
the logo is found with the tongue attached - this is needed and to be quite big if possible – we need the chilli image. It needs to be a good design where our customers and us go WOW.

text of the salts is found on the website.

barcode is needed along the right side. but do not include in the image i will put that on myself

also ingredient list - this is currently not looking any good.

needs to be the "worlds hottest" somewhere
Nice to have
• something clean crisp and elegant like

http://crateloomviews.examplehost.net/2009/10/plain-drop.html

** this is what we would like http://3.img.examplehost.net/_9QwLrTzXpaM/RkPd-7NnvGs/AAAAAAAAH2K/kTr4WZxeLPQ/s1600/KLMV+cards.jpg
clean crisp and
Should not have
• too many fonts

```html
<!DOCTYPE html>
<html lang="en">
<head>
<meta charset="utf-8">
<title>Very Hot BBQ Chilli Salt Label</title>
<link rel="stylesheet" href="https://fonts.googleapis.com/css2?family=Archivo+Black&family=Tinos:wght@400&family=Chewy&display=swap">
<style>
  :root {
    --brown: #9a5213;
    --white: #ffffff;
    --ink: #111111;
    --burst: #f7d324;
    --burst-edge: #d9a90c;
    --red: #e0301e;
    --chilli: #e1251b;
    --chilli-dark: #b3150f;
    --stem: #7cc242;
    --badge: #3f7a2c;
    --badge-dark: #23501a;
  }
  * { margin: 0; padding: 0; box-sizing: border-box; }
  html, body { width: 1200px; height: 467px; overflow: hidden; background: var(--white); }
  .label { position: relative; width: 1200px; height: 467px; background: var(--white); overflow: hidden; }
  .label-bands { position: absolute; inset: 0; }
  .burst { position: absolute; left: 110px; top: 0; width: 240px; height: 205px; }
  .burst-text {
    position: absolute; left: 150px; top: 72px; width: 150px;
    font-family: "Archivo Black", sans-serif; font-size: 21px; line-height: 23px;
    color: var(--red); text-align: center; transform: rotate(-12deg);
  }
  .flavour-name {
    position: absolute; left: 394px; top: 38px;
    font-family: "Archivo Black", sans-serif; font-size: 39px; color: var(--brown);
  }
  .product-name {
    position: absolute; left: 470px; top: 112px;
    font-family: "Archivo Black", sans-serif; font-style: italic; font-size: 62px; line-height: 70px;
    color: var(--white); -webkit-text-stroke: 3px var(--brown); paint-order: stroke fill;
    transform: rotate(-10deg); transform-origin: left top;
  }
  .product-name span { display: block; }
  .product-name .second { margin-left: -50px; }
  .award { position: absolute; left: 848px; top: 80px; width: 178px; height: 124px; }
  .chilli-art {
    position: absolute; left: 24px; top: 222px; width: 190px; height: 172px;
    background: radial-gradient(ellipse at 55% 55%, var(--chilli) 0%, var(--chilli) 55%, var(--chilli-dark) 80%, rgba(255,255,255,0) 82%);
  }
  .weight { position: absolute; left: 43px; top: 426px; font-family: "Tinos", serif; font-size: 18px; color: var(--ink); }
  .description {
    position: absolute; left: 353px; top: 255px; width: 380px;
    font-family: "Tinos", serif; font-size: 24.5px; line-height: 29.5px; color: var(--ink);
  }
  .tagline {
    position: absolute; left: 353px; top: 400px;
    font-family: "Chewy", cursive; font-size: 31px; color: var(--red);
  }
  .brand {
    position: absolute; left: 742px; top: 300px; width: 130px;
    display: flex; flex-direction: column; align-items: center; gap: 8px;
  }
  .brand-mark { width: 22px; height: 22px; border-radius: 50%; background: var(--red); }
  .brand-name { font-family: "Tinos", serif; font-size: 17px; color: var(--ink); }
  .ingredients {
    position: absolute; left: 934px; top: 213px; width: 180px;
    font-family: "Tinos", serif; font-size: 11.5px; line-height: 14.5px; color: var(--ink);
  }
  .contact {
    position: absolute; left: 934px; top: 384px;
    font-family: "Tinos", serif; font-size: 14px; line-height: 23.5px; color: var(--ink);
  }
</style>
</head>
<body>
<main class="label">
  <svg class="label-bands" width="1200" height="467" viewBox="0 0 1200 467" aria-hidden="true">
    <rect x="0" y="0" width="1200" height="8" fill="var(--brown)"/>
    <rect x="1186" y="0" width="14" height="467" fill="var(--brown)"/>
    <path d="M0 112 C 220 110, 380 125, 560 118 C 760 108, 960 70, 1200 52 L 1200 170 C 1000 160, 820 170, 620 195 C 420 222, 200 230, 0 222 Z" fill="var(--brown)"/>
  </svg>

  <svg class="burst" viewBox="0 0 240 205" aria-hidden="true">
    <polygon points="120,8 140,62 190,22 172,80 236,70 188,112 232,148 168,140 178,198 130,152 96,200 90,146 28,178 62,126 4,108 64,90 30,40 90,62" fill="var(--burst)" stroke="var(--burst-edge)" stroke-width="2"/>
  </svg>
  <div class="burst-text">World's Hottest</div>

  <h1 class="flavour-name">Very Hot BBQ</h1>
  <h2 class="product-name"><span>Chilli</span><span class="second">Salt</span></h2>

  <svg class="award" viewBox="0 0 178 124" aria-hidden="true">
    <rect x="20" y="14" width="138" height="96" rx="14" fill="var(--badge)" stroke="var(--badge-dark)" stroke-width="3"/>
  </svg>

  <div class="chilli-art" role="img" aria-label="Illustration of a red chilli pepper"></div>
  <p class="weight">100 Grams</p>

  <p class="description">A robust combination of chilli and spices to add a great boost of flavour. Must be invited to any BBQ or pizza night! Hot</p>
  <p class="tagline">relish the blaze</p>

  <div class="brand">
    <span class="brand-mark"></span>
    <span class="brand-name">Fernmoltaskels</span>
  </div>

  <p class="ingredients">Ingredients:<br>Bhut Jolokia Chilli, Pink Himalayan Rock Salt, Onion, Gralic, Thyme, Pepper, Mustard seed, Corriander and lots more</p>

  <p class="contact">PO Box 482 Marlowe Ridge 6914<br>fernmoltaskels.com<br>Made in WA</p>
</main>
</body>
</html>
```